Help me create an amazing cover for my first ebook!!

I am looking to have a modern and professional looking cover for my first ebook. It will be published through Borvex Quill Self Press and will need to follow their formatting and guidelines. I want the cover to have a modern and vibrant feel, that appeals to a millennial audience. This is a real estate book that is focused on a niche category catered to young professionals, so the idea would be to appeal to them.

Title:
The Twentysomething Playbook for Duplex Living

A Smart Property Buying Plan to Start Early, Cut Your Housing Costs (Sometimes to Zero), and Speed Up Your Path to Lasting Wealth.

Davin Osterlund

Target Market(s)

Real Estate investors, investors, millennials, young professionals, college educated, 20-40 years old.Financial freedom, finance.

Industry/Entity Type

Real Estate

Font styles to use
Sans Serif

Colors

Designer to choose colors to be used in the design.

Requirements
Must have
• Must follow the borvex quill self press format. I attached a screenshot of the details, it can also be found here: https://qsp.borvexbooks.example/en_US/help/topic/R481736025
• Must include this title:
• The Twentysomething Playbook for Duplex Living
• A Smart Property Buying Plan to Start Early, Cut Your Housing Costs (Sometimes to Zero), and Speed Up Your Path to Lasting Wealth.
• Davin Osterlund.
• I added examples of book covers I like to use as a guide, I also added some color pallette examples.
Nice to have
• Modern, clean design that's not too busy. Some sort of simple photo or illustration to incorporate in the cover along with the text would be nice.

```html
<!DOCTYPE html>
<html lang="en">
<head>
<meta charset="utf-8">
<title>The Twentysomething Playbook for Duplex Living — Davin Osterlund</title>
<link rel="stylesheet" href="https://fonts.googleapis.com/css2?family=Baloo+2:wght@700;800&family=Cabin:wght@700&display=swap">
<style>
  :root {
    --ink: #464a59;
    --fog: #f5f4f8;
    --haze: #e4e3ea;
    --mist: #c9c8d0;
    --tower: #6a6c78;
    --tower-dark: #343640;
  }
  html, body {
    margin: 0;
    padding: 0;
    width: 750px;
    height: 1200px;
    overflow: hidden;
    background: var(--fog);
  }
  .cover {
    position: relative;
    width: 750px;
    height: 1200px;
    overflow: hidden;
    color: var(--ink);
    text-align: center;
  }
  .cover-photo {
    position: absolute;
    inset: 0;
    background:
      radial-gradient(ellipse 42% 22% at 62% 8%, rgba(52,54,64,0.95) 0%, rgba(74,76,88,0.8) 45%, rgba(106,108,120,0) 100%),
      radial-gradient(ellipse 30% 26% at 96% 22%, rgba(52,54,64,0.9) 0%, rgba(90,92,104,0.55) 55%, rgba(106,108,120,0) 100%),
      radial-gradient(ellipse 16% 22% at 6% 14%, rgba(52,54,64,0.92) 0%, rgba(90,92,104,0.55) 55%, rgba(106,108,120,0) 100%),
      radial-gradient(ellipse 16% 18% at 98% 45%, rgba(52,54,64,0.9) 0%, rgba(90,92,104,0.5) 55%, rgba(106,108,120,0) 100%),
      radial-gradient(ellipse 14% 22% at 0% 62%, rgba(150,150,160,0.55) 0%, rgba(201,200,208,0) 100%),
      radial-gradient(ellipse 12% 18% at 100% 78%, rgba(170,170,180,0.5) 0%, rgba(201,200,208,0) 100%),
      radial-gradient(ellipse 55% 40% at 50% 62%, var(--fog) 0%, rgba(245,244,248,0.7) 55%, rgba(245,244,248,0) 100%),
      linear-gradient(180deg, var(--haze) 0%, var(--fog) 45%, var(--fog) 100%);
  }
  .title {
    position: absolute;
    left: 0;
    right: 0;
    top: 622px;
    margin: 0;
    font-family: "Baloo 2", sans-serif;
    font-weight: 800;
    text-transform: uppercase;
    line-height: 1;
  }
  .title-main {
    display: block;
    font-size: 60px;
  }
  .title-sub {
    display: block;
    margin-top: 16px;
    font-size: 49px;
  }
  .subtitle {
    position: absolute;
    left: 56px;
    right: 56px;
    top: 780px;
    margin: 0;
    font-family: "Cabin", sans-serif;
    font-weight: 700;
    font-size: 22px;
    line-height: 33px;
  }
  .divider {
    position: absolute;
    left: 343px;
    top: 897px;
  }
  .author {
    position: absolute;
    left: 0;
    right: 0;
    top: 1010px;
    margin: 0;
    font-family: "Baloo 2", sans-serif;
    font-weight: 800;
    font-size: 68px;
    line-height: 1;
    text-transform: uppercase;
  }
</style>
</head>
<body>
  <main class="cover">
    <div class="cover-photo" role="img" aria-label="Upward view of dark glass skyscrapers framing a pale, foggy sky"></div>

    <h1 class="title">
      <span class="title-main">The Twentysomething</span>
      <span class="title-sub">Playbook for Duplex Living</span>
    </h1>

    <p class="subtitle">A Smart Property Buying Plan to Start Early, Cut Your Housing Costs (Sometimes to Zero), &amp; Speed Up Your Path to Lasting Wealth</p>

    <svg class="divider" width="64" height="14" viewBox="0 0 64 14" aria-hidden="true">
      <circle cx="11" cy="7" r="5" fill="var(--ink)"/>
      <circle cx="32" cy="7" r="4.4" fill="none" stroke="var(--ink)" stroke-width="1.4"/>
      <circle cx="52" cy="7" r="5" fill="var(--ink)"/>
    </svg>

    <p class="author">Davin Osterlund</p>
  </main>
</body>
</html>
```